Editable Flyer Layout for MIDWAY SWIFTLINE

to come up with a flyer layout that has editable spots to change promotions from time to time. We are a courier company in Calgary Alberta. Our logos and color schemes can be viewed on our website www.routebrisker.com We are wanting something that fits with website but more of an edge on the print media side. Our website also feature our "Focus" page which will tell you about us and our practices. Please conside this when constructing flyer. We also have additional image files for you if needed.

Thanks !!!!
Updates

Some of these designs are great. Never expected to get so many different results. I will comment on potential designs once we have reviewed all and only after deadline. For now Thanks to all .....!!!!!

Thank you all for your submissions. Some have been eliminated. Those that have not I have sent message to you. The designs look great but need some minor changes. I have sent some suggestions and revert back to you. Please review the notes above on ad (promo) and the editable space.

Thanks Very Much !!!

Tam

Thank You all very much for your submissions. We will be choosing a candidate today. We love this service, you all did awesome.

Thanks
Tam

Target Market(s)

Commerical businesses shipping freight and courier packages.

Industry/Entity Type

It Company

Requirements
Must have
• Flyer must be free of copyright.

```html
<!DOCTYPE html>
<html lang="en">
<head>
<meta charset="utf-8">
<title>Midway Swiftline – Flyer</title>
<link rel="stylesheet" href="https://fonts.googleapis.com/css2?family=Arimo:wght@400;700&family=Comfortaa:wght@300;400&family=Libre+Baskerville:wght@400;700&display=swap">
<style>
  :root {
    --paper: #d8d5c6;
    --paper-light: #e3e0d3;
    --brand-blue: #1b76bc;
    --brand-blue-dark: #135f9c;
    --ink: #1d1d1b;
    --white: #ffffff;
    --cut-white: #f1efe8;
  }
  * { margin: 0; padding: 0; box-sizing: border-box; }
  html, body { width: 1200px; height: 900px; overflow: hidden; background: var(--white); }
  .flyer { position: relative; width: 1200px; height: 900px; font-family: "Arimo", Arial, sans-serif; }
  .flyer-art { position: absolute; inset: 0; }
  .abs { position: absolute; transform-origin: left top; }

  .brand-mark { left: 82px; top: 80px; }
  .brand-mark .name { display: flex; align-items: center; gap: 10px; font-weight: 700; font-size: 34px; color: var(--brand-blue); letter-spacing: -0.5px; }
  .brand-mark .square { width: 26px; height: 26px; background: var(--brand-blue); }
  .brand-mark .tagline { font-size: 13px; font-weight: 700; color: var(--ink); margin: 2px 0 0 62px; }
  .brand-mark .web { font-size: 15px; font-weight: 700; color: var(--brand-blue); margin: 1px 0 0 110px; }

  .terms-note { left: 532px; top: 30px; width: 170px; transform: rotate(20deg); font-family: "Comfortaa", sans-serif; font-weight: 300; font-size: 12px; line-height: 1.25; color: var(--brand-blue); text-align: right; }

  .promo-badge { left: 712px; top: 52px; width: 196px; height: 200px; transform: rotate(12deg); background: var(--brand-blue); border: 4px solid var(--white); border-radius: 12px; box-shadow: 3px 4px 8px rgba(0,0,0,.35); color: var(--white); text-align: center; }
  .promo-badge .top { font-size: 15px; font-weight: 700; margin-top: 16px; }
  .promo-badge .for { font-size: 30px; font-weight: 400; line-height: 1; letter-spacing: 1px; }
  .promo-badge .price { font-size: 88px; font-weight: 700; line-height: 1; }
  .promo-badge .price sup { font-size: 24px; vertical-align: top; }
  .promo-badge .price .dollar { font-size: 38px; vertical-align: top; }
  .promo-badge .fine { font-size: 11px; font-weight: 700; }

  .zone-sign { left: 898px; top: 310px; width: 205px; height: 205px; transform: rotate(22deg); transform-origin: center; background: var(--brand-blue); border: 4px solid var(--white); border-radius: 14px; box-shadow: 3px 4px 8px rgba(0,0,0,.35); }
  .zone-sign .inner { position: absolute; left: 50%; top: 50%; width: 210px; transform: translate(-50%,-50%) rotate(-34deg); text-align: center; color: var(--white); font-weight: 700; }
  .zone-sign .word { font-size: 28px; }
  .zone-sign .plate { background: var(--white); color: var(--brand-blue); border-radius: 6px; margin: 6px 14px; padding: 6px 4px; }
  .zone-sign .plate .n { font-size: 18px; }
  .zone-sign .plate .p { font-size: 11px; color: var(--ink); }

  .pledge { left: 460px; top: 318px; transform: rotate(-12deg); color: var(--brand-blue); }
  .pledge .the { font-size: 20px; font-weight: 700; }
  .pledge .title { font-size: 38px; font-weight: 700; line-height: .9; margin-left: 22px; }
  .pledge .sub { font-size: 20px; font-weight: 700; margin-left: 132px; line-height: .9; }
  .pledge-copy { left: 483px; top: 408px; transform: rotate(-12deg); font-family: "Comfortaa", sans-serif; font-weight: 300; font-size: 17px; line-height: 1.3; color: var(--brand-blue); }

  .welcome-copy { left: 104px; top: 410px; transform: rotate(-16deg); font-family: "Comfortaa", sans-serif; font-weight: 300; font-size: 17px; line-height: 1.3; color: var(--brand-blue); }
  .welcome { left: 130px; top: 497px; transform: rotate(-12deg); color: var(--brand-blue); font-weight: 700; }
  .welcome .title { font-size: 38px; }
  .welcome .sub { font-size: 20px; margin: -6px 0 0 86px; }

  .band-name { left: 78px; top: 618px; transform: rotate(-14deg); color: var(--cut-white); font-weight: 700; }
  .band-name .n { font-size: 66px; letter-spacing: 1px; line-height: 1; text-shadow: 1px 2px 2px rgba(0,0,0,.35); }
  .band-name .t { font-size: 22px; margin: 4px 0 0 120px; text-shadow: 1px 1px 1px rgba(0,0,0,.3); }

  .caution { left: 806px; top: 578px; transform: rotate(-6deg); font-family: "Libre Baskerville", serif; color: var(--cut-white); text-shadow: 1px 2px 2px rgba(0,0,0,.35); }
  .caution .title { font-size: 54px; font-weight: 700; line-height: 1; }
  .caution .sub { font-size: 18px; font-weight: 700; margin-left: -42px; letter-spacing: .5px; }

  .contact { left: 420px; top: 730px; transform: rotate(-6deg); color: var(--brand-blue); font-weight: 700; }
  .contact .c1 { font-size: 24px; margin-left: 22px; line-height: 1; }
  .contact .c2 { font-size: 36px; margin-left: 22px; line-height: .95; }
  .contact address { font-style: normal; font-size: 15px; line-height: 1.45; margin-top: 6px; }
</style>
</head>
<body>
<main class="flyer">
  <svg class="flyer-art" width="1200" height="900" viewBox="0 0 1200 900" aria-hidden="true">
    <defs>
      <radialGradient id="paperTone" cx="50%" cy="45%" r="70%">
        <stop offset="0" stop-color="var(--paper-light)"/>
        <stop offset="1" stop-color="var(--paper)"/>
      </radialGradient>
    </defs>
    <rect x="28" y="8" width="1128" height="876" fill="url(#paperTone)"/>
    <polygon class="band band-top" points="760,120 1156,18 1156,112 800,230" fill="var(--brand-blue)"/>
    <polygon class="band band-caution" points="220,700 1156,505 1156,628 250,716" fill="var(--brand-blue-dark)"/>
    <polygon class="band band-main" points="28,590 930,370 975,505 28,755" fill="var(--brand-blue)"/>
  </svg>

  <header class="abs brand-mark">
    <div class="name"><span class="square"></span>Midway Swiftline</div>
    <div class="tagline">dispatched today, delivered by dawn</div>
    <div class="web">www.routebrisker.com</div>
  </header>

  <p class="abs terms-note">* For just 10 dollars Ship anywhere between Calgary - Lethbridge and Medicine Hat or anywhere point between.<br>Up to a maximum weight of 150lbs<br>Guarranteed Overnight<br>G.S.T. extra<br>NO EXTRA SURCHARGES</p>

  <div class="abs promo-badge">
    <div class="top">Guaranteed Overnight</div>
    <div class="for">FOR JUST!</div>
    <div class="price"><span class="dollar">$</span>10<sup>*</sup></div>
    <div class="fine">* Terms and conditions apply</div>
  </div>

  <div class="abs zone-sign">
    <div class="inner">
      <div class="word">Shipping</div>
      <div class="plate">
        <div class="n">Midway Swiftline</div>
        <div class="p">Toll Free 1.800.555.0142</div>
      </div>
      <div class="word">Zone</div>
    </div>
  </div>

  <h2 class="abs pledge"><div class="the">the</div><div class="title">Swiftline</div><div class="sub">pledge</div></h2>
  <p class="abs pledge-copy">Our guarantee is that<br>your shipment will always<br>arrive when stated.</p>

  <p class="abs welcome-copy">Look to us for a friendly,<br>reliable shipping experience!<br>No extra frees for rush service,<br>we only have rush service!</p>
  <h2 class="abs welcome"><div class="title">Welcome</div><div class="sub">message</div></h2>

  <div class="abs band-name"><div class="n">Midway Swiftline</div><div class="t">dispatched today, delivered by dawn</div></div>

  <div class="abs caution"><div class="title">Caution</div><div class="sub">EXPRESS SHIPPING IN EFFECT</div></div>

  <section class="abs contact">
    <div class="c1">contact</div>
    <div class="c2">Us</div>
    <address>Midway Swiftline<br>410- 88 Harbour Road N.E., Calgary, AB<br>T0X-1Z9 Canada<br>Toll Free: 1.800.555.0142</address>
  </section>
</main>
</body>
</html>
```